Webdesign für ORVI Registrierung für die USA
Zielgruppe
Erstellung von Reisegenehmigungen (Visa)
Aufgabenstellung
- Orientierung an Orvi.us
- es gibt kein Logo oder CD
- die Webseite soll seriös wirken

```html
<!DOCTYPE html>
<html lang="en">
<head>
<meta charset="utf-8">
<title>ORVI – Travel Authorization for the United States</title>
<link href="https://fonts.googleapis.com/css2?family=Libre+Franklin:wght@500;600;700&family=Raleway:wght@400;500;600&display=swap" rel="stylesheet">
<style>
:root{
  --green:#a0b317;
  --green-dark:#8fa012;
  --ink:#333438;
  --text:#4a4b50;
  --muted:#77787c;
  --line:#d9d9d9;
  --dark-band:#333333;
  --footer:#ececec;
  --footer-bar:#dedede;
  --white:#ffffff;
}
*{box-sizing:border-box;margin:0;padding:0}
html,body{width:1200px;height:3367px;overflow:hidden}
body{font-family:"Raleway",sans-serif;color:var(--text);background:var(--white);position:relative}
h1,h2,h3,.brand{font-family:"Libre Franklin",sans-serif}
.abs{position:absolute}
.btn{position:absolute;display:flex;align-items:center;justify-content:center;background:var(--green);color:var(--white);border-radius:20px;font-size:12px;font-weight:600;letter-spacing:.3px;text-transform:uppercase;text-decoration:none}
.btn.shadow{box-shadow:4px 5px 8px rgba(0,0,0,.2)}
.rule{position:absolute;height:2px;width:44px;background:var(--green)}

/* hero */
.hero{position:absolute;left:0;top:0;width:1200px;height:537px;background:linear-gradient(100deg,#6e7480 0%,#8a909a 35%,#7b818c 60%,#5f6671 100%)}
.hero-shade{position:absolute;inset:0;background:rgba(40,45,55,.25)}
.brand{position:absolute;left:98px;top:24px;font-size:30px;font-weight:700;letter-spacing:3px;color:var(--white)}
.nav{position:absolute;top:34px;left:587px;display:flex;gap:37px;font-size:13px;color:var(--white);font-weight:500}
.nav-cta{left:993px;top:29px;width:108px;height:27px;font-size:11px;font-weight:500}
.hero h1{position:absolute;top:160px;left:0;width:1200px;text-align:center;color:var(--white);font-size:29px;font-weight:600}
.hero-sub{position:absolute;top:219px;left:260px;width:680px;text-align:center;color:var(--white);font-size:14.5px;line-height:21px}
.feature{position:absolute;top:330px;width:220px;text-align:center}
.feature .art{margin:0 auto;width:116px;height:116px;border-radius:50%;border:2px solid rgba(255,255,255,.55);background:radial-gradient(circle at 40% 45%,#e7c24a 0%,#3b8ad3 45%,#c9d3dc 46%,rgba(255,255,255,.15) 70%)}
.feature .label{margin-top:24px;color:var(--white);font-size:14.5px;letter-spacing:2px;font-weight:500}

/* eligibility */
.plane-art{left:172px;top:622px;width:136px;height:140px;border-radius:8px;background:linear-gradient(135deg,#f4d56a 0%,#e9e9e9 40%,#cfcfcf 100%)}
.elig h2{position:absolute;left:398px;top:618px;font-size:29px;font-weight:600;color:var(--ink)}
.elig .rule{left:398px;top:671px}
.elig p{position:absolute;left:398px;width:706px;font-size:14.5px;line-height:21px;color:var(--text)}

.contact-band{left:99px;top:977px;width:1002px;height:78px;background:var(--dark-band);color:var(--white);font-size:22px;display:flex;align-items:center;justify-content:center}
.contact-band span{color:var(--green);margin-left:6px}

/* cards */
.card{position:absolute;top:1143px;width:316px;height:380px;border:1px solid #e5e5e5;text-align:center}
.card.active{border-color:var(--green)}
.card svg{margin-top:68px}
.card h3{margin:28px auto 0;width:260px;font-size:17.5px;font-weight:600;color:var(--ink);line-height:21px}
.card.active h3{color:var(--green);text-decoration:underline}
.card p{margin:14px auto 0;width:240px;font-size:12.8px;line-height:21px;color:var(--text)}
.card-btn{position:absolute;top:1503px;width:150px;height:40px;border-radius:20px;border:2px solid #cfcfcf;background:var(--white);color:var(--ink);font-size:12px;letter-spacing:1.5px;font-weight:600;display:flex;align-items:center;justify-content:center}
.card-btn.active{background:var(--green);border-color:var(--green);color:var(--white)}

.divider{left:99px;top:1630px;width:1002px;height:1px;background:var(--line)}

/* service columns */
.col{position:absolute;top:1712px;width:480px}
.col h2{font-size:23px;font-weight:600;color:var(--muted);line-height:30px}
.col h2 em{font-style:normal;color:var(--green)}
.col p{margin-top:30px;font-size:14px;line-height:21px;color:var(--text)}
.checks{list-style:none;margin-top:14px}
.checks li{display:flex;align-items:center;gap:9px;font-size:14px;height:28px;color:var(--text)}
.checks small{font-size:11px;color:var(--muted)}

/* text band */
.text-band{left:0;top:2258px;width:1200px;height:494px;background:linear-gradient(100deg,#4a4f58 0%,#5c616a 50%,#484d56 100%)}
.text-band h2{position:absolute;top:95px;width:1200px;text-align:center;color:var(--white);font-size:29px;font-weight:600}
.text-band .rule{left:578px;top:137px}
.text-band p{position:absolute;left:100px;width:1000px;text-align:center;color:var(--white);font-size:14.5px;line-height:21px}

/* cta */
.cta h2{position:absolute;top:2830px;width:1200px;text-align:center;font-size:29px;font-weight:600;color:var(--muted)}
.cta p{position:absolute;top:2880px;left:230px;width:740px;text-align:center;font-size:14.5px;line-height:21px;color:var(--text)}

/* footer */
.footer{left:0;top:3072px;width:1200px;height:245px;background:var(--footer)}
.foot-links{position:absolute;top:85px;display:flex;flex-direction:column;gap:14px;font-size:11.5px;color:var(--text);text-transform:uppercase}
.help{position:absolute;right:99px;top:83px;text-align:right;color:var(--text)}
.help b{font-size:12px;font-weight:600;color:var(--ink)}
.help .hours{font-size:10.5px;margin-top:6px}
.help .hot{font-size:12px;font-weight:600;color:var(--ink)}
.help .hot span{font-size:18px;font-weight:400;color:var(--green)}
.cards-row{display:flex;gap:8px;justify-content:flex-end;margin-top:12px}
.pay{width:46px;height:27px;border-radius:3px}
.bottom{left:0;top:3317px;width:1200px;height:50px;background:var(--footer-bar)}
.bottom .copy{position:absolute;left:99px;top:19px;font-size:11px;color:var(--text)}
.social{position:absolute;right:99px;top:17px;display:flex;gap:14px}
.social span{width:16px;height:16px;border-radius:50%;background:#7a7b7f}
</style>
</head>
<body>

<header class="hero">
  <div class="abs" role="img" aria-label="Blurred photo of travellers walking through an airport terminal" style="inset:0"></div>
  <div class="hero-shade"></div>
  <div class="brand">ORVI</div>
  <nav class="nav"><span>VISA BUSINESS</span><span>VISA WHAT IS ORVI</span><span>CONTACT</span></nav>
  <a class="btn nav-cta">APPLY NOW</a>
  <h1>Beguiled &amp; demoralized by the charms of pleasure moment.</h1>
  <p class="hero-sub">dignissimos ducimus qui blanditiis praesentium voluptatum deleniti atque corrupti quos dolores et quas molestias excepturi sint occaecati cupiditate non provident.</p>
  <div class="feature" style="left:205px"><div class="art" role="img" aria-label="Illustration of a laptop with a magnifying glass and papers"></div><div class="label">APPLY ONLINE</div></div>
  <div class="feature" style="left:477px"><div class="art" role="img" aria-label="Illustration of a suitcase with travel stickers and a plane"></div><div class="label">TRAVEL TO THE U.S</div></div>
  <div class="feature" style="left:751px"><div class="art" role="img" aria-label="Illustration of a passport and boarding tickets"></div><div class="label">IMMIGRATION</div></div>
</header>

<section class="elig">
  <div class="abs plane-art" role="img" aria-label="Line illustration of a plane flying past the sun and a cloud"></div>
  <h2>FREE ORVI ELIGIBILITY TEST</h2>
  <div class="rule"></div>
  <p style="top:692px">Only citizens of Visa Waiver Countries are allowed to apply for ORVI. It is important to know if you qualify for ORVI before you submit your application. Use the drop-down menu on the left to select your nationality and click on "Submit".</p>
  <p style="top:776px">The ORVI application system is entirely online. There are no forms that need to be printed and you do not have to go to a U.S. Embassy or Consulate in person. Download the ORVI Application Guide and apply today!.</p>
  <a class="btn" style="left:398px;top:862px;width:118px;height:30px;font-weight:500">APPLY NOW</a>
</section>

<div class="abs contact-band">Please submit the form contact us via email at: <span>info@orvi.us</span></div>

<section class="cards">
  <article class="card" style="left:99px">
    <svg width="96" height="70" viewBox="0 0 96 70" fill="none" stroke="#a0b317" stroke-width="2.5" stroke-linecap="round" stroke-linejoin="round">
      <path d="M28 4a24 22 0 1 0 0 44 24 22 0 0 0 8-1l12 8-3-12A22 20 0 0 0 28 4z"/>
      <path d="M23 19a6 6 0 1 1 7 6v5M30 37v1"/>
      <path d="M48 22h44v34H60l-12 10 3-10h-3z" fill="#fff"/>
      <path d="M60 40l7 7 14-15"/>
    </svg>
    <h3>WHAT IS ORVI?</h3>
    <p>ORVI stands for Online Registration for Visa Information. ORVI is an online application system developed by the United States government to. . .</p>
  </article>
  <article class="card active" style="left:442px">
    <svg width="80" height="70" viewBox="0 0 80 70" fill="none" stroke="#a0b317" stroke-width="2.5" stroke-linecap="round" stroke-linejoin="round">
      <path d="M4 22l14-14 10 8M76 22L62 8 50 16"/>
      <path d="M18 8l-6 30 14 14M62 8l6 30-22 22-18-18 14-14 10 6"/>
      <path d="M26 52l6 6M32 46l8 8M38 40l8 8"/>
      <path d="M40 2v6M28 4l3 5M52 4l-3 5"/>
    </svg>
    <h3>WHO NEEDS TO APPLY<br>FOR ORVI?</h3>
    <p>All travelers entering the United States (by air or sea) under the visa waiver program are required to hold a valid. . .</p>
  </article>
  <article class="card" style="left:785px">
    <svg width="60" height="70" viewBox="0 0 60 70" fill="none" stroke="#a0b317" stroke-width="2.5" stroke-linecap="round" stroke-linejoin="round">
      <path d="M6 2h48v50L40 66H6z"/>
      <path d="M40 66V52h14"/>
      <circle cx="30" cy="20" r="10"/><circle cx="30" cy="17" r="4"/><path d="M23 27a8 6 0 0 1 14 0"/>
      <path d="M14 40h32M14 47h20M14 56h2M20 56h2M26 56h2"/>
    </svg>
    <h3>WHAT IS THE VISA WAIVER PROGRAM?</h3>
    <p>The visa waiver program is a U.S. govern-ment program that enables citizens and nationals from the Visa Waiver. . .</p>
  </article>
  <a class="card-btn" style="left:183px">READ MORE</a>
  <a class="card-btn active" style="left:525px">READ MORE</a>
  <a class="card-btn" style="left:868px">READ MORE</a>
</section>

<div class="abs divider"></div>

<section class="col" style="left:99px">
  <h2>Verify - Locate - Check<br>Status of your <em>ORVI</em> Travel Authorization</h2>
  <p>Do you already have an existing travel authorization but got questions? We can assist you with the following:</p>
  <ul class="checks">
    <li><svg width="16" height="16" viewBox="0 0 16 16" fill="none" stroke="#a0b317" stroke-width="1.6"><path d="M14 7.5A6.5 6.5 0 1 1 10.5 2"/><path d="M5 7.5l3 3 7-7"/></svg>Receive help to verify your ORVI</li>
    <li><svg width="16" height="16" viewBox="0 0 16 16" fill="none" stroke="#a0b317" stroke-width="1.6"><path d="M14 7.5A6.5 6.5 0 1 1 10.5 2"/><path d="M5 7.5l3 3 7-7"/></svg>Receive help to locate your existing travel authorization (ORVI)</li>
    <li><svg width="16" height="16" viewBox="0 0 16 16" fill="none" stroke="#a0b317" stroke-width="1.6"><path d="M14 7.5A6.5 6.5 0 1 1 10.5 2"/><path d="M5 7.5l3 3 7-7"/></svg>Check the status of your travel authorization</li>
  </ul>
</section>
<a class="btn shadow" style="left:99px;top:1978px;width:102px;height:30px;font-weight:500">CONTINUE</a>

<section class="col" style="left:614px">
  <h2>Update an existing ORVI<br>before flying to the <em>United States</em></h2>
  <p>Travelers with an approved travel authorization (ORVI) may update their own travel authorization before each trip to the United States. The following information can be changed before each trip:</p>
  <ul class="checks">
    <li><svg width="16" height="16" viewBox="0 0 16 16" fill="none" stroke="#a0b317" stroke-width="1.6"><path d="M14 7.5A6.5 6.5 0 1 1 10.5 2"/><path d="M5 7.5l3 3 7-7"/></svg>Email address</li>
    <li><svg width="16" height="16" viewBox="0 0 16 16" fill="none" stroke="#a0b317" stroke-width="1.6"><path d="M14 7.5A6.5 6.5 0 1 1 10.5 2"/><path d="M5 7.5l3 3 7-7"/></svg>Telephone number</li>
    <li><svg width="16" height="16" viewBox="0 0 16 16" fill="none" stroke="#a0b317" stroke-width="1.6"><path d="M14 7.5A6.5 6.5 0 1 1 10.5 2"/><path d="M5 7.5l3 3 7-7"/></svg>Airline you are flying with</li>
    <li><svg width="16" height="16" viewBox="0 0 16 16" fill="none" stroke="#a0b317" stroke-width="1.6"><path d="M14 7.5A6.5 6.5 0 1 1 10.5 2"/><path d="M5 7.5l3 3 7-7"/></svg>Flight number</li>
    <li><svg width="16" height="16" viewBox="0 0 16 16" fill="none" stroke="#a0b317" stroke-width="1.6"><path d="M14 7.5A6.5 6.5 0 1 1 10.5 2"/><path d="M5 7.5l3 3 7-7"/></svg>City where you are boarding</li>
    <li><svg width="16" height="16" viewBox="0 0 16 16" fill="none" stroke="#a0b317" stroke-width="1.6"><path d="M14 7.5A6.5 6.5 0 1 1 10.5 2"/><path d="M5 7.5l3 3 7-7"/></svg>Address while in the United States&nbsp;<small>(unless if transit through the U.S.)</small></li>
  </ul>
  <p style="margin-top:16px">We can assist you in updating and verifying your travel authorization before departure.</p>
</section>
<a class="btn shadow" style="left:613px;top:2140px;width:120px;height:30px;font-weight:500">UPDATE ORVI</a>

<section class="abs text-band" role="img" aria-label="Darkened photo of travellers with luggage in a terminal hall">
  <h2>UNDERTAKES LABORIOUS PHYSICAL EXERCISE</h2>
  <div class="rule"></div>
  <p style="top:166px">At vero eos et accusamus et iusto odio dignissimos ducimus qui blanditiis praesentium voluptatum deleniti atque corrupti quos dolores et quas molestias excepturi sint occaecati cupiditate non provident, similique sunt in culpa qui officia deserunt mollitia animi, id est laborum et dolorum fuga. Et harum quidem rerum facilis est et expedita distinctio. Nam libero tempore, cum soluta nobis est eligendi optio cumque nihil impedit quo minus id quod maxime placeat facere possimus, omnis voluptas assumenda est, omnis dolor repellendus. Temporibus autem quibusdam et aut officiis debitis aut rerum necessitatibus saepe eveniet ut et voluptates repudiandae sint et molestiae non recusandae. Itaque earum rerum hic tenetur a sapiente delectus, ut aut reiciendis voluptatibus maiores alias consequatur aut perferendis doloribus asperiores repellat.</p>
  <p style="top:314px">On the other hand, we denounce with righteous indignation and dislike men who are so beguiled and demoralized by the charms of pleasure of the moment, so blinded by desire, that they cannot foresee the pain and trouble that are bound to ensue; and equal blame belongs to those who fail in their duty through weakness of will, which is the same as saying through shrinking from toil and pain. These cases are perfectly simple and easy to distinguish. In a free hour, when our power of choice is untrammelled and when nothing prevents our being able to do what we like best, every pleasure is to be welcomed and every pain avoided.</p>
</section>

<section class="cta">
  <h2>DUCIMUS QUI BLANDITIIS PRAESENTIUM</h2>
  <p>Righteous indignation and dislike men who are so beguiled and demoralized by the charms of pleasure of the moment, so blinded by desire</p>
  <a class="btn" style="left:525px;top:2945px;width:150px;height:40px;letter-spacing:1.5px">APPLY NOW</a>
</section>

<footer class="abs footer">
  <div class="foot-links" style="left:99px"><span>Start Page</span><span>Tourist Visa</span><span>Business Visa</span></div>
  <div class="foot-links" style="left:262px"><span>What is ORVI</span><span>Conditions</span><span>Contact</span></div>
  <div class="help">
    <b>Sie Brauchen Hilfe?</b>
    <div class="hours">Service Hotline Von Mo-Fr 10-16 Uhr</div>
    <div class="hot">Kostenfrei: <span>0800 555 0199</span></div>
    <div class="cards-row"><span class="pay" style="background:#2f6fb5"></span><span class="pay" style="background:#d8452e"></span><span class="pay" style="background:#ffffff;border:1px solid #d0d0d0"></span></div>
  </div>
</footer>
<div class="abs bottom">
  <div class="copy">© 2017 ORVI, ALL RIGHTS RESERVED</div>
  <div class="social"><span></span><span></span><span></span></div>
</div>

</body>
</html>
```